Fahrzeugbeschriftung für Brandschutzservice
Zielgruppe
Siehe bitte www.lorventa.de
Aufgabenstellung
Brandschutzservice / Kundendienst / Feuerlöscher vor Ort beim Kunden prüfen /

```html
<!DOCTYPE html>
<html lang="de">
<head>
<meta charset="utf-8">
<title>Lorventa GmbH – Fahrzeugbeschriftung</title>
<link href="https://fonts.googleapis.com/css2?family=Roboto+Condensed:wght@400;700&family=Rubik:wght@400&display=swap" rel="stylesheet">
<style>
  :root {
    --brand-red: #c8161d;
    --ink: #1a1a1a;
    --paper: #f4f4f2;
    --body-white: #ffffff;
    --body-line: #c9c9c9;
    --glass: #d9dde0;
    --tyre: #2b2b2b;
    --rim: #b8bcc0;
    --flame-a: #f6c24a;
    --flame-b: #e8731d;
    --flame-c: #c9301a;
  }
  * { margin: 0; padding: 0; box-sizing: border-box; }
  html, body { width: 1200px; height: 848px; overflow: hidden; background: var(--paper); }
  .canvas { position: relative; width: 1200px; height: 848px; }
  .vehicle { position: absolute; left: 0; top: 0; width: 1200px; height: 848px; }

  .service-band {
    position: absolute; left: 241px; top: 380px; width: 695px; height: 42px;
    background: var(--brand-red); color: #fff;
    font-family: "Rubik", sans-serif; font-size: 17px;
  }
  .service-band span { position: absolute; top: 10px; white-space: nowrap; }
  .band-customer { left: 40px; }
  .band-services { left: 239px; }
  .band-divider { position: absolute; left: 222px; top: 0; width: 2px; height: 42px; background: rgba(255,255,255,.6); }

  .brand-mark { position: absolute; left: 520px; top: 300px; width: 54px; height: 54px; background: var(--brand-red); }
  .brand-name {
    position: absolute; left: 600px; top: 300px;
    font-family: "Roboto Condensed", sans-serif; font-weight: 700;
    font-size: 40px; line-height: 54px; color: var(--brand-red); letter-spacing: .5px;
  }

  .contact {
    position: absolute; left: 284px; top: 448px;
    font-family: "Roboto Condensed", sans-serif; color: var(--ink); font-size: 12.5px; line-height: 15px;
  }
  .contact-name { font-weight: 700; font-size: 18px; line-height: 22px; color: var(--brand-red); }
  .contact-gap { margin-top: 5px; }

  .flames {
    position: absolute; left: 282px; top: 450px; width: 432px; height: 125px;
    background: linear-gradient(to top, var(--flame-c) 0%, var(--flame-b) 35%, var(--flame-a) 70%, rgba(246,194,74,0) 100%);
    opacity: .85; z-index: 0;
  }
  .contact { z-index: 1; }
</style>
</head>
<body>
<main class="canvas">
  <svg class="vehicle" viewBox="0 0 1200 848" aria-hidden="true">
    <path d="M120,575 L120,420 Q124,392 165,380 L260,345 Q310,262 345,250 L940,240 Q978,242 986,282 L998,520 L1004,575 L870,575 A72,72 0 0 0 726,575 L278,575 A72,72 0 0 0 134,575 Z"
          fill="var(--body-white)" stroke="var(--body-line)" stroke-width="2"/>
    <path d="M280,372 L330,280 Q345,262 365,262 L452,262 L442,380 Z" fill="var(--glass)"/>
    <line x1="464" y1="262" x2="464" y2="570" stroke="var(--body-line)" stroke-width="1.5"/>
    <line x1="241" y1="378" x2="241" y2="570" stroke="var(--body-line)" stroke-width="1.5"/>
    <circle cx="206" cy="575" r="62" fill="var(--tyre)"/>
    <circle cx="206" cy="575" r="34" fill="var(--rim)"/>
    <circle cx="798" cy="575" r="62" fill="var(--tyre)"/>
    <circle cx="798" cy="575" r="34" fill="var(--rim)"/>
  </svg>

  <div class="flames" role="img" aria-label="Flammen-Illustration in Gelb, Orange und Rot entlang der unteren Fahrzeugseite"></div>

  <div class="brand-mark"></div>
  <div class="brand-name">Lorventa GmbH</div>

  <div class="service-band">
    <span class="band-customer">Kundendienst</span>
    <div class="band-divider"></div>
    <span class="band-services">Brandschutzservice &nbsp;&amp;&nbsp; Feuerlöscher &amp; Rauchmelder</span>
  </div>

  <address class="contact" style="font-style:normal">
    <div class="contact-name">Lorventa GmbH</div>
    <div>Lindenweg 12 · 07745 Feldhain</div>
    <div class="contact-gap">Tel: 03641 55210</div>
    <div>lorventa.de</div>
  </address>
</main>
</body>
</html>
```